Tressvane hair oil bottle & packaging (Instagrammable)

I'm a blogger/social media influencer and I'm launching my own hair oil that I created myself. The hair oil is something I've used fora a long time and it makes your hair grow like there's no tomorrow!

I'm looking for a feminine and minimalistic bottle for the hair oil and also a nice packaging for the bottle. Please have a look at my Instagram account (@minaveltroo), I'd love if the product design and color scheme would be inspired by my Instagram feed. I'm looking for a design that would look very 'Instagrammable'

Product name: Tressvane
Bottle size: 100ml

Thank you xx

Target Market(s)

Females

Requirements
Must have
• According to the law this has to be marked on the packaging and on the bottle:
• Amount: 100ml
• Marked on the packaging:
• Ingredients: Burdock root oil, Grapeseed oil, Organic castor oil (maybe somehow draw attention to the fact that it's organic when designing the bottle & packaging), peppermint oil, Lavender oil, Cedarwood oil, Rosemary oil
Nice to have
• I added some photos of Ai Wenna packaging - I absolutely love it! The colour is exactly what I have in mind (also if you check my Instagram it's kind of my 'feed colour' - I'd be happy if the packaging would look something like that. The Ai Wenna packaging is exactly what I meant by 'Instagrammable'.
• Also - if we go for something like this, we could write Glow up! on the inside (so you see that when opening the packaging) or feel free to come up with something yourself, just bear in mind it's a hair oil that promotes hair growth

```html
<!DOCTYPE html>
<html lang="en">
<head>
<meta charset="utf-8">
<title>Tressvane hair oil bottles</title>
<link rel="stylesheet" href="https://fonts.googleapis.com/css2?family=Forum&family=EB+Garamond:ital@1&display=swap">
<style>
  :root {
    --backdrop: #bfbfbf;
    --bottle: #0a090b;
    --cap-line: #0a090b;
    --label: #fcebef;
    --ink: #3a3438;
  }
  html, body {
    margin: 0;
    padding: 0;
    overflow: hidden;
  }
  .canvas {
    position: relative;
    width: 1200px;
    height: 1200px;
    background: var(--backdrop);
    overflow: hidden;
  }
  .bottle {
    position: absolute;
  }
  .bottle__cap {
    position: absolute;
    box-sizing: border-box;
    border: 4px solid var(--cap-line);
    border-bottom: none;
    border-radius: 2px 2px 0 0;
  }
  .bottle__cap::after {
    content: "";
    position: absolute;
    top: 0;
    bottom: 0;
    left: 50%;
    width: 4px;
    margin-left: -4px;
    background: var(--cap-line);
  }
  .bottle__body {
    position: absolute;
    background: var(--bottle);
    border-radius: 6px;
  }
  .label {
    position: absolute;
    background: var(--label);
    border-radius: 4px;
    overflow: hidden;
  }
  .label__stroke {
    position: absolute;
    inset: 0;
  }
  .label__wordmark {
    position: absolute;
    left: 0;
    right: 0;
    top: 96px;
    text-align: center;
    font-family: "Forum", serif;
    font-size: 24px;
    color: var(--ink);
  }
  .label__wordmark span {
    border-bottom: 1.5px solid var(--ink);
    padding: 0 1px 2px;
  }
  .label__list {
    position: absolute;
    inset: 0;
    margin: 0;
    padding: 0;
    list-style: none;
  }
  .label__list li {
    position: absolute;
    left: 0;
    right: 0;
    text-align: center;
    font-family: "EB Garamond", serif;
    font-style: italic;
    font-size: 9px;
    line-height: 12px;
    color: var(--ink);
    text-decoration: underline;
    text-underline-offset: 2px;
  }
</style>
</head>
<body>
<main class="canvas">

  <section class="bottle bottle--front" aria-label="Front of bottle">
    <div class="bottle__cap" style="left:310px; top:274px; width:74px; height:120px;"></div>
    <div class="bottle__body" style="left:218px; top:394px; width:265px; height:486px;"></div>
    <div class="label" style="left:265px; top:478px; width:158px; height:286px;">
      <svg class="label__stroke" viewBox="0 0 158 286" role="img" aria-label="Soft lilac watercolour brush stroke">
        <defs>
          <linearGradient id="stroke-front" x1="0" y1="0" x2="1" y2="1">
            <stop offset="0" stop-color="#b9a6c0" stop-opacity="0.9"/>
            <stop offset="0.5" stop-color="#c9b8cc" stop-opacity="0.75"/>
            <stop offset="1" stop-color="#b09cb8" stop-opacity="0.9"/>
          </linearGradient>
        </defs>
        <rect x="-30" y="118" width="330" height="54" rx="27" fill="url(#stroke-front)" transform="rotate(62 79 143)"/>
      </svg>
      <div class="label__wordmark"><span>Tressvane</span></div>
    </div>
  </section>

  <section class="bottle bottle--back" aria-label="Back of bottle">
    <div class="bottle__cap" style="left:690px; top:284px; width:71px; height:112px;"></div>
    <div class="bottle__body" style="left:597px; top:395px; width:269px; height:490px; transform:rotate(0.4deg);"></div>
    <div class="label" style="left:658px; top:474px; width:152px; height:298px;">
      <svg class="label__stroke" viewBox="0 0 152 298" role="img" aria-label="Soft lilac watercolour brush stroke">
        <defs>
          <linearGradient id="stroke-back" x1="0" y1="0" x2="1" y2="1">
            <stop offset="0" stop-color="#b9a6c0" stop-opacity="0.9"/>
            <stop offset="0.5" stop-color="#c9b8cc" stop-opacity="0.75"/>
            <stop offset="1" stop-color="#b09cb8" stop-opacity="0.9"/>
          </linearGradient>
        </defs>
        <rect x="-40" y="122" width="340" height="50" rx="25" fill="url(#stroke-back)" transform="rotate(64 76 149)"/>
      </svg>
      <ul class="label__list">
        <li style="top:24px;">Ingredients</li>
        <li style="top:54px;">Burdock root oil</li>
        <li style="top:80px;">Grapeseed oil</li>
        <li style="top:106px;">Organic castor oil</li>
        <li style="top:132px;">Peppermint oil</li>
        <li style="top:158px;">Lavender oil</li>
        <li style="top:184px;">Cedarwood oil</li>
        <li style="top:210px;">Rosemary oil</li>
        <li style="top:261px;">100ml</li>
      </ul>
    </div>
  </section>

</main>
</body>
</html>
```